Podiatry clinic requires a modern revamp and editing of existing website.

I would like a fresh new look and updated information for my current business website. An easy to navigate site with prominent address and phone number for call to action. We are a podiatry clinic that focuses on general and sports podiatry.
I would like 4 pages; including Home page, About Us, Services & Contact.
www.brambleridgefootcare.com

Target Market(s)

Active working professionals.

Industry/Entity Type

Medical

Coding

Coded - Design and coding required

Number of Pages Required

4 page

Font styles to use
Sans Serif

Colors
6b449b

Requirements
Must have
• A modern look with logo and active images; clean and uncluttered. Visible phone number and address for call to action.
• 4 pages - Home, About Us, Services, Contact.
• Home page - update address & service logos.
• About Us - update of personal information.
• Services - Revamp of existing page.
• Contact page to include Google map, email & phone number.
Nice to have
• Ability to add content easily; eg. a blog or adding video onto Home page.
• Link to Facebook page.

```html
<!DOCTYPE html>
<html lang="en">
<head>
<meta charset="utf-8">
<title>Brambleridge Foot Care</title>
<link href="https://fonts.googleapis.com/css2?family=Open+Sans:wght@400;600;700&display=swap" rel="stylesheet">
<style>
:root{
  --purple:#6b449b;
  --purple-light:#8b6cc0;
  --purple-dark:#55357f;
  --ink:#333;
  --muted:#666;
  --dark:#2a2a2a;
  --darker:#1c1c1c;
  --page:#f6f6f6;
  --white:#fff;
  --tab-cyan:#4aa6d6;
  --tab-blue:#6b86cc;
  --tab-pink:#c8508a;
  --tab-amber:#dca23e;
  --tab-violet:#9b80d0;
}
*{box-sizing:border-box;margin:0;padding:0}
html,body{width:1200px;height:2560px;overflow:hidden}
body{position:relative;background:var(--page);font-family:"Open Sans",Arial,sans-serif;color:var(--ink)}
.abs{position:absolute}
/* header */
.site-header{left:0;top:0;width:1200px;height:97px;background:#242424}
.brand{left:178px;top:0;width:124px;height:97px;background:var(--purple-light);display:flex;align-items:center;justify-content:center;text-align:center;color:var(--white);font-weight:700;font-size:17px;line-height:1.15;padding:0 8px}
.topline{top:20px;right:172px;font-size:12px;color:var(--white);display:flex;gap:22px;align-items:center}
.topline span{display:flex;align-items:center;gap:6px}
.nav{top:66px;left:644px;display:flex;gap:30px;font-size:12.5px;color:var(--white);font-weight:600;letter-spacing:.2px}
.nav .active{color:#b9a0e4}
.search{left:1009px;top:63px;width:32px;height:32px;background:var(--purple);display:flex;align-items:center;justify-content:center}
/* hero */
.hero{left:0;top:97px;width:1200px;height:514px;background:linear-gradient(100deg,#6f6a66 0%,#a49c95 35%,#cfc6bd 55%,#8c6a78 75%,#5e5550 100%)}
.hero-arrow{top:290px;width:30px;height:31px;background:var(--purple);display:flex;align-items:center;justify-content:center}
.hero-title{left:198px;top:280px;font-size:36px;font-weight:700;line-height:1.3;color:var(--white)}
.hero-title em{font-style:normal;color:var(--purple)}
.hero-btn{left:203px;top:389px;width:111px;height:39px;background:#111;color:var(--white);font-size:14px;display:flex;align-items:center;justify-content:center}
/* info boxes */
.info{top:558px;height:193px;width:285px;color:var(--white);padding:12px 26px}
.info h2{font-weight:400;font-size:22px;line-height:1.1;margin-bottom:16px}
.info p{font-size:12.5px;line-height:1.45}
.info-row{display:flex;gap:14px;font-size:12.5px;line-height:1.45;margin-bottom:16px}
.map{width:222px;height:88px;background:linear-gradient(135deg,#e9eef2,#dfe6d9);margin-top:10px}
/* welcome */
.section-title{font-size:22px;font-weight:400;text-align:center;width:1200px;left:0}
.rule{height:2px;background:#ccc;width:140px;left:530px}
.rule::after{content:"";position:absolute;left:54px;top:0;width:32px;height:2px;background:var(--purple)}
.welcome-text{left:172px;top:938px;width:460px;font-size:12.5px;line-height:1.5;color:#444}
.welcome-text p{margin-bottom:17px}
.welcome-text strong{font-size:15px;color:#222}
.mini-arrows{display:flex;gap:2px}
.mini-arrows span{width:14px;height:14px;border:1px solid #aaa;background:var(--white);display:flex;align-items:center;justify-content:center}
.video{left:688px;top:927px;width:340px;height:239px;background:linear-gradient(120deg,#d8c6c0,#eee5e2 45%,#c9b4b4)}
.video-caption{left:0;bottom:0;width:100%;height:43px;background:var(--purple-light);color:var(--white);font-size:15px;display:flex;align-items:center;justify-content:center}
.play{left:148px;top:100px;width:44px;height:30px;background:#d32c2c;border-radius:7px;display:flex;align-items:center;justify-content:center}
/* services */
.services{left:0;top:1203px;width:1200px;height:300px;background:var(--white)}
.service{top:62px;width:190px;text-align:center}
.service h3{font-size:14px;font-weight:400;letter-spacing:.3px;margin-bottom:20px}
.service-icon{width:58px;height:58px;margin:0 auto 22px;background:var(--purple);border-radius:50% 50% 12px 50%;opacity:.9}
.service p{font-size:11.5px;line-height:1.6;color:#777;text-align:justify}
/* blog + problems */
.lower{left:0;top:1503px;width:1200px;height:432px;background:var(--white)}
.block-title{font-size:28px;font-weight:400;color:#222}
.block-rule{height:1px;background:#ddd}
.block-rule::after{content:"";position:absolute;left:0;top:-1px;width:40px;height:3px;background:var(--purple)}
.post{left:172px;width:412px}
.thumb{width:62px;height:58px;background:linear-gradient(135deg,#d9b79f,#f0ddd0)}
.post h4{font-size:15px;font-weight:400;color:#222;margin-bottom:6px}
.meta{font-size:10.5px;color:#666;display:flex;gap:26px;margin-bottom:8px}
.meta span{display:flex;gap:5px;align-items:center}
.post p{font-size:11px;line-height:1.55;color:#555}
.post a{color:var(--purple);text-decoration:none}
.tab{top:67px;width:29px;height:321px;color:var(--white);display:flex;flex-direction:column;align-items:center;justify-content:space-between;padding:6px 0}
.tab .label{writing-mode:vertical-rl;transform:rotate(180deg);font-size:12px;white-space:nowrap}
.panel{left:654px;top:67px;width:229px;height:321px;padding:0 0 0 12px}
.panel-img{width:146px;height:108px;background:linear-gradient(135deg,#9fb6c9,#dfe7ee 50%,#b8a89a)}
.panel h5{font-size:12.5px;font-weight:600;margin:14px 0 10px}
.panel p{font-size:11px;line-height:1.6;color:#555}
.panel .more{display:inline-block;margin-top:12px;border:1px solid #aaa;font-size:10px;padding:6px 9px}
/* partners */
.partners{left:0;top:1935px;width:1200px;height:267px;background:#f4f4f4}
.badge{top:131px;height:50px;background:#c9c9c9;border-radius:4px}
/* footer */
.footer{left:0;top:2202px;width:1200px;height:307px;background:var(--dark);border-top:4px solid var(--purple);color:#bbb}
.fcol{top:20px;width:196px}
.fcol h6{font-size:16px;font-weight:400;color:var(--white);padding-bottom:10px;border-bottom:1px solid #555;margin-bottom:14px;position:relative}
.fcol h6::after{content:"";position:absolute;left:0;bottom:-1px;width:120px;height:1px;background:var(--purple-light)}
.fline{font-size:11.5px;line-height:1.5;color:#aaa;padding:10px 0;border-bottom:1px solid #444;display:flex;gap:10px}
.input{height:28px;background:#1f1f1f;border:1px solid #3a3a3a;font-size:11px;color:#777;padding:6px 10px;margin-bottom:10px}
.btn{background:var(--purple);color:var(--white);font-size:11px;padding:6px 0;width:74px;text-align:center}
.avatar{width:68px;height:58px;background:linear-gradient(135deg,#b8aaa5,#e8e0dc)}
.copyright{left:0;top:2509px;width:1200px;height:51px;background:var(--darker);color:#ccc;font-size:11.5px;padding:17px 0 0 184px}
.to-top{left:998px;top:2530px;width:31px;height:30px;background:var(--purple);display:flex;align-items:center;justify-content:center}
</style>
</head>
<body>

<header class="abs site-header">
  <div class="abs brand">Brambleridge Foot Care</div>
  <div class="abs topline">
    <span>Have any queries?</span>
    <span><svg width="11" height="11" viewBox="0 0 24 24"><path fill="#b9a0e4" d="M6.6 10.8a15 15 0 0 0 6.6 6.6l2.2-2.2c.3-.3.7-.4 1-.2 1.1.4 2.3.6 3.6.6.6 0 1 .4 1 1V20c0 .6-.4 1-1 1A17 17 0 0 1 3 4c0-.6.4-1 1-1h3.5c.6 0 1 .4 1 1 0 1.3.2 2.5.6 3.6.1.3 0 .7-.2 1z"/></svg>Contact Us : 1300 555 274</span>
    <span><svg width="12" height="10" viewBox="0 0 24 18"><rect x="1" y="1" width="22" height="16" fill="none" stroke="#b9a0e4" stroke-width="2"/><path d="M1 1l11 9 11-9" fill="none" stroke="#b9a0e4" stroke-width="2"/></svg>info@brambleridgefootcare.com</span>
  </div>
  <nav class="abs nav"><span class="active">HOME</span><span>ABOUT US</span><span>SERVICES</span><span>CONTACT US</span></nav>
  <div class="abs search"><svg width="15" height="15" viewBox="0 0 24 24"><circle cx="10" cy="10" r="7" fill="none" stroke="#fff" stroke-width="3"/><path d="M15 15l7 7" stroke="#fff" stroke-width="3"/></svg></div>
</header>

<section class="abs hero" role="img" aria-label="Close-up photo of a runner's shoe striking a gravel path"></section>
<div class="abs hero-arrow" style="left:108px"><svg width="10" height="14" viewBox="0 0 10 14"><path d="M8 1L2 7l6 6" fill="none" stroke="#fff" stroke-width="3"/></svg></div>
<div class="abs hero-arrow" style="left:1062px"><svg width="10" height="14" viewBox="0 0 10 14"><path d="M2 1l6 6-6 6" fill="none" stroke="#fff" stroke-width="3"/></svg></div>
<h1 class="abs hero-title"><em>Walking</em> is The Best<br>Exercise for Your Feet</h1>
<div class="abs hero-btn">Learn More</div>

<div class="abs info" style="left:172px;background:var(--purple)">
  <h2>Why Choose Us</h2>
  <p>Our podiatrists are fully qualified health professionals.<br>We provide General Podiatry Treatment , Sports Injuries, Orthotic Therapy and Nail Surgery.</p>
</div>
<div class="abs info" style="left:457px;background:var(--purple-light)">
  <h2>Locate Us</h2>
  <div class="info-row" style="margin-bottom:0;gap:10px;padding-left:4px"><svg width="10" height="13" viewBox="0 0 10 14"><path d="M5 0a5 5 0 0 0-5 5c0 4 5 9 5 9s5-5 5-9a5 5 0 0 0-5-5zm0 7a2 2 0 1 1 0-4 2 2 0 0 1 0 4z" fill="#fff"/></svg><span>Suite 210 / 85 Harlow Street<br>Eastvale 3000</span></div>
  <div class="map" role="img" aria-label="Street map showing the clinic location"></div>
</div>
<div class="abs info" style="left:742px;width:286px;background:var(--purple-dark)">
  <h2>Make<br>An Appointment</h2>
  <div class="info-row"><svg width="11" height="11" viewBox="0 0 24 24"><path fill="#fff" d="M6.6 10.8a15 15 0 0 0 6.6 6.6l2.2-2.2c.3-.3.7-.4 1-.2 1.1.4 2.3.6 3.6.6.6 0 1 .4 1 1V20c0 .6-.4 1-1 1A17 17 0 0 1 3 4c0-.6.4-1 1-1h3.5c.6 0 1 .4 1 1 0 1.3.2 2.5.6 3.6.1.3 0 .7-.2 1z"/></svg><span>Phone :<br>1300 555 274</span></div>
  <div class="info-row"><svg width="12" height="10" viewBox="0 0 24 18"><rect x="1" y="1" width="22" height="16" fill="none" stroke="#fff" stroke-width="2"/><path d="M1 1l11 9 11-9" fill="none" stroke="#fff" stroke-width="2"/></svg><span>Email :<br>info@brambleridgefootcare.com</span></div>
</div>

<h2 class="abs section-title" style="top:812px">Welcome To Brambleridge Foot Care</h2>
<div class="abs rule" style="top:853px"></div>

<div class="abs welcome-text">
  <p><strong>Brambleridge Foot Care</strong> is a Podiatry clinic in the heart of Eastvale CBD. We are located between Harlow &amp; Grant Streets in the Meridian Business Centre / Parkside Hotel Complex.</p>
  <p>Our podiatrists are fully qualified health professionals who are able to diagnose, treat, manage or help to prevent all medical conditions that affect the feet and lower limb.</p>
  <p>We provide General Podiatry Treatment and some Specialised Services in relation to various foot conditions, including Sports Injuries, Orthotic Therapy and Nail Surgery.</p>
</div>
<div class="abs mini-arrows" style="left:995px;top:901px"><span><svg width="5" height="7" viewBox="0 0 5 7"><path d="M5 0L0 3.5 5 7z" fill="#333"/></svg></span><span><svg width="5" height="7" viewBox="0 0 5 7"><path d="M0 0l5 3.5L0 7z" fill="#333"/></svg></span></div>
<div class="abs video" role="img" aria-label="Video still of a gloved clinician treating a toenail">
  <div class="abs play"><svg width="12" height="14" viewBox="0 0 12 14"><path d="M0 0l12 7-12 7z" fill="#fff"/></svg></div>
  <div class="abs video-caption">Nail Surgery Procedure</div>
</div>

<section class="abs services">
  <div class="abs service" style="left:172px"><h3>HEEL PAIN</h3><div class="service-icon" role="img" aria-label="Heel pain icon"></div><p>Common condition that causes pain around the heel or arch area that is caused by factors such as faulty foot biomechanics [...]</p></div>
  <div class="abs service" style="left:394px"><h3>SHIN SPLINTS</h3><div class="service-icon" role="img" aria-label="Shin splints icon"></div><p>Faulty foot biomechanics or injuries can cause excessive strain and damage to soft tissues like muscles &amp; tendons or bones &amp; joints [...]</p></div>
  <div class="abs service" style="left:616px"><h3>NAIL SURGERY</h3><div class="service-icon" role="img" aria-label="Nail surgery icon"></div><p>Minor surgical procedure for the permanent removal of ingrown toenails under local anaesthesia [...]</p></div>
  <div class="abs service" style="left:838px"><h3>ORTHOTIC THERAPY</h3><div class="service-icon" role="img" aria-label="Orthotic therapy icon"></div><p>Orthoses, or arch supports, are designed to control the function of the foot when there is evidence of faulty biomechanics [...]</p></div>
</section>

<section class="abs lower">
  <h2 class="abs block-title" style="left:172px;top:5px">Latest Blog Post</h2>
  <div class="abs mini-arrows" style="left:553px;top:22px"><span><svg width="5" height="7" viewBox="0 0 5 7"><path d="M5 0L0 3.5 5 7z" fill="#333"/></svg></span><span><svg width="5" height="7" viewBox="0 0 5 7"><path d="M0 0l5 3.5L0 7z" fill="#333"/></svg></span></div>
  <div class="abs block-rule" style="left:172px;top:49px;width:418px"></div>

  <article class="abs post" style="top:67px;display:flex;gap:12px">
    <div class="thumb" role="img" aria-label="Photo of a foot being examined"></div>
    <div style="width:338px"><h4>Why Do Heel Spurs Occur?</h4>
      <div class="meta"><span><svg width="10" height="10" viewBox="0 0 10 10"><rect x="0" y="1" width="10" height="9" fill="#7a5aa8"/></svg>Aug 02. 2016</span><span><svg width="11" height="9" viewBox="0 0 11 9"><path d="M0 0h11v6H4L1 9V6H0z" fill="#7a5aa8"/></svg>6 Comments</span></div>
      <p>These bony protrusions are commonly found in association with a condition called Plantar Fasciitis. Plantar Fasciitis occurs when the plantar fascia ligament, which spans the arch of the foot, becomes stressed, torn and inflamed <a>[...]</a></p></div>
  </article>
  <article class="abs post" style="top:230px;display:flex;gap:12px">
    <div class="thumb" role="img" aria-label="Photo of a hand massaging a sore foot"></div>
    <div style="width:338px"><h4>What is Plantar Fasciitis?</h4>
      <div class="meta"><span><svg width="10" height="10" viewBox="0 0 10 10"><rect x="0" y="1" width="10" height="9" fill="#7a5aa8"/></svg>Aug 01. 2016</span><span><svg width="11" height="9" viewBox="0 0 11 9"><path d="M0 0h11v6H4L1 9V6H0z" fill="#7a5aa8"/></svg>11 Comments</span></div>
      <p>The term "Plantar Fasciitis" is literally translated as "Foot Inflammation". It is a progressive condition if left untreated, the combination of excessive movement of the ligament, small tears,inflammation and possible bone spurs can become debilitating to the sufferer <a>[...]</a></p></div>
  </article>

  <h2 class="abs block-title" style="left:623px;top:5px">Common Foot Problems</h2>
  <div class="abs block-rule" style="left:623px;top:49px;width:405px"></div>

  <div class="abs tab" style="left:625px;background:var(--tab-cyan)"><span>&#8211;</span><span class="label">Tarsal Bones Coalition Treatment</span><span>&#9633;</span></div>
  <div class="abs panel">
    <div class="panel-img" role="img" aria-label="Photo of a clinician reviewing a foot x-ray with a patient"></div>
    <h5>Tarsal Bones Coalition Treatment</h5>
    <p>Tarsal coalition is an abnormal connection of two or more bones in the foot. The bones affected — called tarsal bones — are located toward the back of the foot and in the heel, and the connection of the bones can result in a severe, rigid flatfoot.</p>
    <span class="more">Learn More</span>
  </div>
  <div class="abs tab" style="left:884px;background:var(--tab-cyan)"><span>+</span><span class="label">Paralytic Deformity Correction</span><span>&#9825;</span></div>
  <div class="abs tab" style="left:913px;background:var(--tab-blue)"><span>+</span><span class="label">Peroneal Tendinitis</span><span>&#9633;</span></div>
  <div class="abs tab" style="left:942px;background:var(--tab-pink)"><span>+</span><span class="label">Diabetic Foot Deformities</span><span>&#215;</span></div>
  <div class="abs tab" style="left:971px;background:var(--tab-amber)"><span>+</span><span class="label">Insertional Achilles Tendinitis</span><span>&#9633;</span></div>
  <div class="abs tab" style="left:1000px;background:var(--tab-violet)"><span>+</span><span class="label">Hallux Rigidus</span><span>&#9675;</span></div>
</section>

<section class="abs partners">
  <h2 class="abs section-title" style="top:35px;font-size:27px">Our Partners</h2>
  <div class="abs rule" style="top:79px;left:518px;width:164px"></div>
  <div class="abs badge" style="left:178px;width:150px"></div>
  <div class="abs badge" style="left:358px;width:132px"></div>
  <div class="abs badge" style="left:522px;width:128px"></div>
  <div class="abs badge" style="left:688px;width:122px"></div>
  <div class="abs badge" style="left:830px;width:195px"></div>
</section>

<footer class="abs footer">
  <div class="abs fcol" style="left:172px"><h6>Contact</h6>
    <div class="fline" style="padding-top:0">Brambleridge Foot Care is a Podiatry clinic in the heart of Eastvale CBD</div>
    <div class="fline"><span style="color:var(--purple-light)">&#9679;</span><span>Suite 210 / 85 Harlow Street<br>Eastvale 3000</span></div>
    <div class="fline"><span style="color:var(--purple-light)">&#9990;</span>1300 555 274</div>
    <div class="fline" style="border:0"><span style="color:var(--purple-light)">&#9993;</span>info@brambleridgefootcare.com</div>
  </div>
  <div class="abs fcol" style="left:393px"><h6>Quick Contact</h6>
    <div class="input">Name...</div><div class="input">Email...</div><div class="input" style="height:70px">Message...</div>
    <div class="btn" style="margin-left:120px">SUBMIT</div>
  </div>
  <div class="abs fcol" style="left:611px"><h6>Testimonials</h6>
    <div style="display:flex;gap:10px;align-items:center;margin-bottom:12px"><div class="avatar" role="img" aria-label="Portrait photo of a client"></div><span style="color:#ddd;font-size:13px">Nora Whitfield</span></div>
    <p style="font-size:11px;line-height:1.6;color:#aaa">Sed ut perspiciatis unde omnis iste natus error sit vo accusantium doloremque laudantium, totam re aperiam, eaque ipsa quae ab illo inventore veritatis et quasi architecto beatae.</p>
    <div class="mini-arrows" style="margin:10px 0 0 150px"><span><svg width="5" height="7" viewBox="0 0 5 7"><path d="M5 0L0 3.5 5 7z" fill="#333"/></svg></span><span><svg width="5" height="7" viewBox="0 0 5 7"><path d="M0 0l5 3.5L0 7z" fill="#333"/></svg></span></div>
  </div>
  <div class="abs fcol" style="left:831px;top:12px"><h6 style="border:0">Newsletter</h6>
    <p style="font-size:12px;line-height:1.5;color:#ccc;margin-bottom:14px">Subscribe to our newsletter for latest updates</p>
    <div class="input" style="height:30px">Email...</div>
    <div class="btn" style="margin-left:120px;margin-bottom:14px">SUBMIT</div>
    <div class="btn" style="width:184px;margin-left:12px;background:#3d4f9e;padding:8px 0">Connect on our social page</div>
  </div>
</footer>
<div class="abs copyright">© Copyright information here</div>
<div class="abs to-top"><svg width="12" height="8" viewBox="0 0 12 8"><path d="M0 8l6-7 6 7z" fill="#fff"/></svg></div>

</body>
</html>
```